PRVD Traditional Business Card Project

Please see attached....just a simple business card... on attachment- please use the exact font, style, etc as the attached "Pat Everard Wynne" card... however, replace with the "Owen Reginald Talbot" text and address below the card.

```html
<!DOCTYPE html>
<html lang="en">
<head>
<meta charset="utf-8">
<title>PRVD Business Card – Owen Reginald Talbot</title>
<link rel="stylesheet" href="https://fonts.googleapis.com/css2?family=Tinos:wght@700&family=Montserrat:wght@600&display=swap">
<style>
  :root {
    --page-bg: #f1f1f0;
    --card-bg: #e8e7e4;
    --brand-blue: #2f5a72;
    --ink-grey: #6f6f6f;
    --rule-grey: #7a7a7a;
  }
  * { margin: 0; padding: 0; box-sizing: border-box; }
  html, body {
    width: 1200px;
    height: 1028px;
    overflow: hidden;
    background: var(--page-bg);
  }
  .business-card {
    position: absolute;
    left: 75px;
    top: 214px;
    width: 1050px;
    height: 600px;
    background: var(--card-bg);
  }
  .firm-name {
    position: absolute;
    top: 44px;
    left: 0;
    width: 100%;
    text-align: center;
    font-family: "Tinos", "Times New Roman", serif;
    font-weight: 700;
    color: var(--brand-blue);
    font-variant: small-caps;
  }
  .firm-name__main {
    display: block;
    font-size: 74px;
    line-height: 1;
  }
  .firm-name__sub {
    display: block;
    margin-top: 4px;
    font-size: 30px;
    letter-spacing: 4px;
    line-height: 1.1;
  }
  .attorney {
    position: absolute;
    top: 236px;
    left: 0;
    width: 100%;
    text-align: center;
  }
  .attorney__name {
    font-family: "Tinos", "Times New Roman", serif;
    font-weight: 700;
    font-variant: small-caps;
    font-size: 60px;
    line-height: 1;
    color: var(--brand-blue);
  }
  .attorney__title {
    margin-top: 4px;
    font-family: "Montserrat", Arial, sans-serif;
    font-weight: 600;
    font-size: 25px;
    letter-spacing: 1px;
    color: var(--ink-grey);
  }
  .contact {
    font-family: "Montserrat", Arial, sans-serif;
    font-weight: 600;
    font-size: 24px;
    line-height: 35.5px;
    color: var(--ink-grey);
    position: absolute;
    top: 438px;
  }
  .contact--address {
    right: 530px;
    text-align: right;
  }
  .contact--lines {
    left: 607px;
  }
  .contact__web,
  .contact__label { color: var(--brand-blue); }
  .contact__email { text-transform: none; }
  .contact-divider {
    position: absolute;
    left: 561px;
    top: 447px;
    width: 2px;
    height: 92px;
    background: var(--rule-grey);
  }
</style>
</head>
<body>
  <div class="business-card">
    <div class="firm-name">
      <span class="firm-name__main">Pacific Ridge</span>
      <span class="firm-name__sub">Legal Group, PLC</span>
    </div>

    <div class="attorney">
      <div class="attorney__name">Owen Reginald Talbot</div>
      <div class="attorney__title">ATTORNEY AT LAW</div>
    </div>

    <div class="contact contact--address">
      <div>4270 CEDAR STREET, SUITE B</div>
      <div>MAPLE GROVE, CA 90210</div>
      <div class="contact__web">www.lawprvd.com</div>
    </div>

    <div class="contact-divider"></div>

    <div class="contact contact--lines">
      <div><span class="contact__label">TEL :</span> (555) 214-7300</div>
      <div><span class="contact__label">FAX :</span> (555) 214-7391</div>
      <div><span class="contact__label">E:</span> <span class="contact__email">otalbot@lawprvd.com</span></div>
    </div>
  </div>
</body>
</html>
```